Real Estate - Property Management Prospectus/Brochure

We need a prospectus made up, around 9-10 pages including the cover page pages 3 onwards can be all a similar template happy for the front cover to have lots of black. I would like it to look very classy and futuristic, high end, blacks, silvers and whites, i am specializing in managing high end rental properties. i would like to design to correspond with the logo. I need to be able to email this booklet mostly - and also be able to print and mail out as well. I would like it crisp and clean as well - not to much on a page. Please note - happy for the cover to be simple with the logo added - prefer lots of black and with the other pages - they can all be a similar layout template to make this job easier? My website is www.tallowquay.com.au and phone is 0471 382 519 email is morva@tallowquay.com.au
Target Market(s)
Investors
Industry/Entity Type
Real Estate
Requirements
Should not have
- Bright greens or bold colours

```html
<!DOCTYPE html>
<html lang="en">
<head>
<meta charset="utf-8">
<title>Tallow Quay – Prospectus Spreads</title>
<link rel="stylesheet" href="https://fonts.googleapis.com/css2?family=Lato:wght@400;700&family=Roboto+Condensed:wght@300;400&display=swap">
<style>
  :root {
    --ink: #000000;
    --paper: #ffffff;
    --silver-light: #f2f2f2;
    --silver-mid: #c9c9c9;
    --silver-dark: #8c8c8c;
    --stage: #e4e4e4;
    --text-soft: #e8e8e8;
    --text-muted: #bdbdbd;
  }
  * { margin: 0; padding: 0; box-sizing: border-box; }
  html, body { width: 1072px; height: 1200px; overflow: hidden; }
  body {
    background: var(--stage);
    font-family: "Lato", sans-serif;
    position: relative;
  }
  .spread {
    position: absolute;
    left: 136px;
    width: 800px;
    height: 540px;
    overflow: hidden;
    box-shadow: 0 6px 18px rgba(0,0,0,0.25);
  }
  .spread--cover { top: 40px; background: var(--ink); }
  .spread--inside { top: 620px; background: var(--ink); }
  .spread svg.cover-shapes { position: absolute; inset: 0; }

  /* logo stand-in */
  .brand {
    position: absolute;
    display: flex;
    align-items: center;
    gap: 8px;
    font-family: "Lato", sans-serif;
    font-weight: 400;
    color: var(--paper);
    letter-spacing: 0.18em;
    text-transform: uppercase;
  }
  .brand__mark { display: block; background: var(--paper); }
  .brand--back { left: 28px; top: 492px; font-size: 13px; color: var(--ink); }
  .brand--back .brand__mark { width: 9px; height: 9px; background: var(--ink); }
  .brand--front { left: 476px; top: 440px; font-size: 21px; }
  .brand--front .brand__mark { width: 14px; height: 14px; }

  .contact {
    position: absolute;
    left: 232px;
    top: 488px;
    font-size: 9.5px;
    line-height: 1.35;
    color: var(--paper);
  }
  .web-front {
    position: absolute;
    left: 476px;
    top: 484px;
    font-size: 12px;
    letter-spacing: 0.14em;
    color: var(--text-muted);
  }
  .spine {
    position: absolute;
    left: 399px; top: 0;
    width: 2px; height: 100%;
    background: linear-gradient(to right, rgba(255,255,255,0.04), rgba(0,0,0,0.35));
  }

  /* inside */
  .city-photo {
    position: absolute;
    inset: 0;
    background:
      linear-gradient(to bottom,
        #3a3a3a 0%, #5a5a5a 18%, #4a4a4a 30%,
        #d8d8d8 42%, #6e6e6e 48%, #1c1c1c 52%,
        #8a8a8a 58%, #2a2a2a 66%, #0e0e0e 78%, #000 100%);
  }
  .column {
    position: absolute;
    top: 404px;
    width: 340px;
    color: var(--text-soft);
  }
  .column--left { left: 32px; }
  .column--right { left: 437px; }
  .column__title {
    font-family: "Roboto Condensed", sans-serif;
    font-weight: 300;
    font-size: 19px;
    color: var(--paper);
    margin-bottom: 10px;
  }
  .column__body {
    font-size: 9.6px;
    line-height: 1.32;
    text-align: justify;
  }
</style>
</head>
<body>

  <section class="spread spread--cover" aria-label="Cover spread">
    <svg class="cover-shapes" viewBox="0 0 800 540" width="800" height="540" aria-hidden="true">
      <defs>
        <linearGradient id="silverLeft" x1="0" y1="0" x2="1" y2="1">
          <stop offset="0" stop-color="var(--silver-light)"/>
          <stop offset="0.5" stop-color="#e0e0e0"/>
          <stop offset="1" stop-color="#b8b8b8"/>
        </linearGradient>
        <linearGradient id="silverRight" x1="0" y1="0" x2="1" y2="1">
          <stop offset="0" stop-color="#b5b5b5"/>
          <stop offset="0.35" stop-color="#ececec"/>
          <stop offset="0.7" stop-color="#d3d3d3"/>
          <stop offset="1" stop-color="#a8a8a8"/>
        </linearGradient>
        <linearGradient id="edge" x1="0" y1="0" x2="0" y2="1">
          <stop offset="0" stop-color="#ffffff"/>
          <stop offset="1" stop-color="#7a7a7a"/>
        </linearGradient>
      </defs>
      <!-- back cover silver panel -->
      <polygon points="0,0 50,0 218,540 0,540" fill="url(#silverLeft)"/>
      <polygon points="50,0 56,0 224,540 218,540" fill="url(#edge)"/>
      <!-- front cover silver panel -->
      <polygon role="img" aria-label="Faceted silver geometric texture" points="563,0 800,0 800,540 765,540" fill="url(#silverRight)"/>
      <polygon points="557,0 563,0 765,540 759,540" fill="url(#edge)"/>
    </svg>
    <div class="spine"></div>

    <div class="brand brand--back"><span class="brand__mark"></span>Tallowquay</div>
    <div class="contact">
      <p>P: 0471 382 519</p>
      <p>E: morva@tallowquay.com.au</p>
      <p>W: www.tallowquay.com.au</p>
    </div>

    <div class="brand brand--front"><span class="brand__mark"></span>Tallowquay</div>
    <p class="web-front">www.tallowquay.com.au</p>
  </section>

  <section class="spread spread--inside" aria-label="Inside spread">
    <div class="city-photo" role="img" aria-label="Black and white night photograph of a city skyline reflected in still water"></div>
    <div class="spine"></div>

    <article class="column column--left">
      <h2 class="column__title">Introduction</h2>
      <p class="column__body">Tallow Quay was founded on the belief that investment property management should deliver results that go beyond our client's expectations. Tallow Quay is building a reputation by excelling in every aspect of the property management process, bringing innovation, confidence, and creativeness with an unparalleled commitment to excellence, these values echo in all aspects of Tallow Quay.</p>
    </article>

    <article class="column column--right">
      <h2 class="column__title">Meeting me – introduction to staff?? Principal/director</h2>
      <p class="column__body">Morva is an industry expert with a history of excellence in property management, with over 12 years experience and a track record of success. Morva approaches her career with intensity, originality and enthusiasm. Her forward-thinking, innovative attitude offers clients a professional, efficient and a friendly management experience.</p>
    </article>
  </section>

</body>
</html>
```